Verdant Ledger - Paid Surveys publisher portal

• Homepage
• Blank Sub Page (Where content goes in between the header/footer)
• Publisher Application Page, complete with Form
• Survey Wall page

Sites that are in a similar vertical that have interesting designs:
brimtolu.com
quastrel.com
vorn.com
pab.io

This is a business-to-business site, and needs to have this type of feel to it. Focus on generating revenue, offer completion, paid surveys is the market.

Format: HTML/CSS

Link to current version of application, and form:
https://tallymarsh.qevrobend.com
https://tallymarsh.qevrobend.com/apply
https://tallymarsh.qevrobend.com/panel/4/drovak_user

Please note that we are changing the brand of this project, the name will be determined shortly but everything else remains. It will likely be Verdant Ledger instead of TallyMarsh. We will confirm.

Industry/Entity Type

Market Research

Coding

Coded - Design and coding required

Number of Pages Required

4 page

Font styles to use
Sans Serif

Colors

Designer to choose colors to be used in the design.

```html
<!DOCTYPE html>
<html lang="en">
<head>
<meta charset="utf-8">
<title>TallyMarsh – Paid Surveys Publisher Portal</title>
<link href="https://fonts.googleapis.com/css2?family=Poppins:wght@400;500;600;700&family=Open+Sans:wght@400;600;700&display=swap" rel="stylesheet">
<style>
:root{
  --red:#e8463d;
  --red-dark:#d23a31;
  --ink:#222222;
  --text:#4a4a4a;
  --muted:#777777;
  --panel:#f4eeee;
  --light:#f3f3f3;
  --dark:#1d1f24;
  --footer:#262626;
  --white:#ffffff;
}
*{margin:0;padding:0;box-sizing:border-box}
html,body{width:1200px;height:4100px;overflow:hidden}
body{font-family:"Open Sans",Arial,sans-serif;color:var(--text);background:var(--white);position:relative}
.section{position:absolute;left:0;width:1200px}
.heading{font-family:"Poppins",Arial,sans-serif;font-weight:600;color:var(--ink)}
.btn{display:inline-block;background:var(--red);color:var(--white);font-family:"Poppins",Arial,sans-serif;font-weight:600;text-transform:uppercase;text-align:center;position:absolute}
.rule{width:52px;height:3px;background:var(--white);position:absolute;left:574px}

/* hero */
.hero{top:0;height:703px;background:linear-gradient(120deg,#6d6256 0%,#a79b8d 35%,#c8c0b6 55%,#6f6a65 80%,#3f4448 100%)}
.logo{position:absolute;display:flex;align-items:center;gap:12px;font-family:"Poppins",Arial,sans-serif;font-weight:600}
.logo-dot{width:42px;height:42px;border-radius:50%}
.hero .logo{left:135px;top:18px;color:var(--white);font-size:27px}
.hero .logo-dot{background:var(--white)}
.nav{position:absolute;top:24px;left:510px;display:flex;font-family:"Poppins",Arial,sans-serif;font-weight:600;font-size:13px;color:var(--white)}
.nav a{color:inherit;text-decoration:none;padding:6px 12px;margin-right:22px}
.nav a.active{background:var(--white);color:var(--ink)}
.hero-copy{position:absolute;left:787px;top:412px;color:var(--white)}
.hero-copy .pre{font-family:"Poppins",Arial,sans-serif;font-weight:600;font-size:30px;line-height:1}
.hero-copy .title{font-family:"Poppins",Arial,sans-serif;font-weight:700;font-size:54px;line-height:1;margin-top:10px}
.hero-copy .lead{font-size:20px;line-height:28px;margin-top:14px;width:330px}
.hero .btn{left:787px;top:604px;width:128px;height:38px;line-height:38px;font-size:14px}
.dots{position:absolute;display:flex;gap:14px;align-items:center}
.dots span{width:9px;height:9px;border-radius:50%;background:var(--white)}
.dots span.on{width:13px;height:13px;background:transparent;border:2px solid var(--white)}
.hero .dots{left:545px;top:624px}

/* about */
.about{top:703px;height:532px;background:var(--white)}
.about-art{position:absolute;left:131px;top:76px;width:378px;height:372px;background:linear-gradient(135deg,#f3d9d6 0%,#e8837b 55%,#c9c9c9 100%)}
.about-panel{position:absolute;left:514px;top:76px;width:552px;height:374px;background:var(--panel)}
.about-panel .kicker{position:absolute;left:60px;top:58px;font-size:17px}
.about-panel .brand{position:absolute;left:60px;top:82px;font-family:"Poppins",Arial,sans-serif;font-weight:700;font-size:38px;color:var(--red)}
.about-panel p{position:absolute;left:60px;top:162px;width:440px;font-size:14px;line-height:21px;color:var(--text)}
.about-panel .btn{left:60px;top:295px;width:104px;height:32px;line-height:32px;font-size:11px}

/* services */
.services{top:1235px;height:626px;background:linear-gradient(120deg,#1a1c21 0%,#2c2f36 45%,#23262c 70%,#14161a 100%);color:var(--white);text-align:center}
.services .heading{color:var(--white);font-size:30px;position:absolute;top:72px;width:100%}
.services .rule{top:128px}
.service{position:absolute;top:214px;width:300px;margin-left:-150px}
.service svg{display:block;margin:0 auto;height:90px}
.service h3{font-family:"Poppins",Arial,sans-serif;font-weight:600;font-size:20px;margin-top:44px}
.service p{font-size:13px;line-height:19px;color:#d7d7d7;margin:20px auto 0;width:250px}
.service .btn{position:static;margin-top:30px;width:125px;height:32px;line-height:32px;font-size:13px}

/* resources */
.resources{top:1861px;height:716px;background:var(--light)}
.resources .heading{position:absolute;top:64px;width:100%;text-align:center;font-size:30px}
.arrow{position:absolute;top:380px}
.card{position:absolute;background:var(--white);box-shadow:0 2px 10px rgba(0,0,0,.08)}
.card .thumb{width:100%}
.card .body{padding:16px 30px}
.card .tag{font-family:"Poppins",Arial,sans-serif;font-weight:600;color:var(--red);font-size:11px}
.card h4{font-family:"Poppins",Arial,sans-serif;font-weight:500;color:var(--ink);font-size:15px;line-height:20px;margin-top:6px}
.card p{font-size:12px;line-height:17px;color:var(--muted);margin-top:10px}
.card .btn{position:static;margin-top:16px;width:66px;height:22px;line-height:22px;font-size:9px}
.card.side{top:246px;width:282px;height:356px}
.card.side .thumb{height:137px;background:linear-gradient(135deg,#c6ccd1,#8c98a3 50%,#d8dcdf)}
.card.main{top:211px;left:435px;width:325px;height:426px}
.card.main .thumb{height:175px;background:linear-gradient(120deg,#e7e8ea 0%,#b9bcc1 55%,#6f7278 100%)}
.card.main h4{font-size:19px;line-height:26px}
.card.main p{font-size:14px;line-height:20px}
.card.main .btn{width:90px;height:28px;line-height:28px;font-size:11px}

/* testimonials */
.testimonials{top:2577px;height:511px;background:linear-gradient(110deg,#e8524a 0%,#f2786c 45%,#e9574d 75%,#d6463e 100%);color:var(--white);text-align:center}
.testimonials .heading{color:var(--white);position:absolute;top:62px;width:100%;font-size:30px}
.testimonials .rule{top:116px}
.quote-mark{position:absolute;left:322px;top:142px;font-family:"Poppins",Arial,sans-serif;font-weight:700;font-size:80px;line-height:1}
.testimonials blockquote{position:absolute;left:350px;top:206px;width:500px;font-size:16px;line-height:22px}
.testimonials .divider{position:absolute;left:455px;top:330px;width:290px;height:1px;background:rgba(255,255,255,.8)}
.testimonials .name{position:absolute;top:365px;width:100%;font-family:"Poppins",Arial,sans-serif;font-weight:600;font-size:15px}
.testimonials .place{position:absolute;top:393px;width:100%;font-size:12px}
.testimonials .dots{left:574px;top:451px;gap:8px}
.testimonials .dots span{width:7px;height:7px}
.testimonials .dots span.on{width:9px;height:9px;border-width:2px}

/* stats */
.stats{top:3088px;height:145px;background:var(--white);display:flex}
.stat{flex:1;text-align:center;border-right:1px solid #e4e4e4;padding-top:32px}
.stat:last-child{border-right:none}
.stat strong{display:block;font-family:"Poppins",Arial,sans-serif;font-weight:600;font-size:42px;line-height:48px;color:var(--red)}
.stat span{font-size:13px;color:var(--ink)}

/* cta */
.cta{top:3233px;height:517px;background:var(--white)}
.cta-photo{position:absolute;right:0;top:0;width:760px;height:517px;background:linear-gradient(90deg,rgba(255,255,255,1) 0%,rgba(255,255,255,0) 30%),linear-gradient(135deg,#5c6068 0%,#2d3038 40%,#8a4b3b 70%,#c9c9cc 100%)}
.cta h2{position:absolute;left:150px;top:118px;width:440px;font-family:"Poppins",Arial,sans-serif;font-weight:400;font-size:27px;line-height:40px;color:var(--ink)}
.cta p{position:absolute;left:150px;top:232px;width:360px;font-size:13px;line-height:19px;color:var(--text)}
.cta .btn{left:150px;top:351px;width:152px;height:44px;line-height:44px;font-size:15px}

/* footer */
.footer{top:3750px;height:350px;background:var(--footer);color:#dcdcdc}
.footer .logo{left:160px;top:122px;color:var(--white);font-size:27px}
.footer .logo-dot{background:var(--red)}
.footer h5{position:absolute;top:62px;font-family:"Poppins",Arial,sans-serif;font-weight:600;font-size:12px;color:var(--white)}
.f-contact{position:absolute;left:481px;top:96px;font-size:11px;line-height:15px}
.f-contact li{list-style:none;display:flex;gap:12px;margin-bottom:16px}
.f-contact svg{flex:none;margin-top:1px}
.f-menu{position:absolute;left:754px;top:96px;font-size:11px;line-height:15px;list-style:none}
.f-social{position:absolute;left:943px;top:96px;font-size:11px;list-style:none}
.f-social li{display:flex;align-items:center;gap:12px;margin-bottom:16px}
.f-social i{width:24px;height:24px;border-radius:50%;background:#3b6fd0;display:block}
.copyright{position:absolute;top:300px;width:100%;text-align:center;font-size:11px;color:#cfcfcf}
</style>
</head>
<body>

<header class="section hero" role="img" aria-label="Photo of a person working on a laptop at a wooden desk with a coffee cup and phone">
  <div class="logo"><span class="logo-dot"></span>TallyMarsh</div>
  <nav class="nav">
    <a class="active">HOME</a><a>ABOUT US</a><a>SERVICES</a><a>SOLUTIONS</a><a>FEATURES</a><a>CONTACT US</a>
  </nav>
  <div class="hero-copy">
    <div class="pre">WELCOME TO THE</div>
    <div class="title">TALLY MARSH</div>
    <div class="lead">Lorem Ipsum is simply dummy text of the printing.</div>
  </div>
  <a class="btn">Read More</a>
  <div class="dots"><span></span><span></span><span class="on"></span><span></span><span></span></div>
</header>

<section class="section about">
  <div class="about-art" role="img" aria-label="Illustration of a red gear with a wrench, symbolising setup and tools"></div>
  <div class="about-panel">
    <div class="kicker heading">ABOUT US</div>
    <div class="brand">TALLY MARSH</div>
    <p>Sed ut perspiciatis unde omnis iste natus error sit volupta tem accusantium doloremque laudantium, totam rem aperiam, eaque ipsa quae ab illo inventore veritatis et quasi architecto beatae vitae dicta sunt explicabo. Nemo enim ipsam voluptatem quia voluptas sit aspernatur aut odit aut fugit.</p>
    <a class="btn">Read More</a>
  </div>
</section>

<section class="section services">
  <h2 class="heading">OUR SERVICES</h2>
  <div class="rule"></div>
  <div class="service" style="left:271px">
    <svg viewBox="0 0 90 90" width="90" fill="none" stroke="#fff" stroke-width="4"><circle cx="38" cy="38" r="26"/><line x1="57" y1="57" x2="82" y2="82" stroke-width="9" stroke-linecap="round"/><text x="38" y="48" font-size="30" fill="#fff" stroke="none" text-anchor="middle" font-family="Poppins,sans-serif" font-weight="600">$</text></svg>
    <h3>Generating Revenue</h3>
    <p>Sed ut perspiciatis unde omnis iste natus error sit volupta tem accusantium doloremque laudantium, totam rem aperiam, eaque ipsa quae ab</p>
    <a class="btn">Read More</a>
  </div>
  <div class="service" style="left:599px">
    <svg viewBox="0 0 100 90" width="100" fill="none" stroke="#fff" stroke-width="4"><circle cx="18" cy="18" r="10"/><circle cx="18" cy="62" r="10"/><line x1="26" y1="24" x2="62" y2="52"/><line x1="26" y1="56" x2="62" y2="24"/><rect x="54" y="34" width="40" height="40" stroke-dasharray="7 5"/></svg>
    <h3>Offer Completion</h3>
    <p>Sed ut perspiciatis unde omnis iste natus error sit volupta tem accusantium doloremque laudantium, totam rem aperiam, eaque ipsa quae ab</p>
    <a class="btn">Read More</a>
  </div>
  <div class="service" style="left:927px">
    <svg viewBox="0 0 70 90" width="70"><rect x="4" y="10" width="62" height="78" rx="4" fill="#fff"/><rect x="22" y="2" width="26" height="14" rx="3" fill="#fff" stroke="#23262c" stroke-width="3"/><g fill="#23262c"><rect x="14" y="30" width="7" height="7"/><rect x="27" y="31" width="28" height="4"/><rect x="14" y="48" width="7" height="7"/><rect x="27" y="49" width="28" height="4"/><rect x="14" y="66" width="7" height="7"/><rect x="27" y="67" width="28" height="4"/></g></svg>
    <h3>Paid surveys</h3>
    <p>Sed ut perspiciatis unde omnis iste natus error sit volupta tem accusantium doloremque laudantium, totam rem aperiam, eaque ipsa quae ab</p>
    <a class="btn">Read More</a>
  </div>
</section>

<section class="section resources">
  <h2 class="heading">RESOURCES</h2>
  <svg class="arrow" style="left:50px" width="14" height="24" viewBox="0 0 14 24"><polyline points="12,2 2,12 12,22" fill="none" stroke="#555" stroke-width="2"/></svg>
  <svg class="arrow" style="left:1136px" width="14" height="24" viewBox="0 0 14 24"><polyline points="2,2 12,12 2,22" fill="none" stroke="#555" stroke-width="2"/></svg>
  <article class="card side" style="left:112px">
    <div class="thumb" role="img" aria-label="Photo of financial newspaper pages"></div>
    <div class="body"><div class="tag">NEWS</div><h4>Lorem Ipsum is simply dummy text of the printing</h4><p>Sed ut perspiciatis unde omnis iste natus error sit volupta tem accusa ntium doloremque</p><a class="btn">Read More</a></div>
  </article>
  <article class="card main">
    <div class="thumb" role="img" aria-label="Photo of a hand drawing a rising red bar chart"></div>
    <div class="body"><div class="tag">NEWS</div><h4>Lorem Ipsum is simply dummy text of the printing</h4><p>Sed ut perspiciatis unde omnis iste natus error sit volupta tem accusa ntium doloremque</p><a class="btn">Read More</a></div>
  </article>
  <article class="card side" style="left:801px">
    <div class="thumb" role="img" aria-label="Photo of financial newspaper pages"></div>
    <div class="body"><div class="tag">NEWS</div><h4>Lorem Ipsum is simply dummy text of the printing</h4><p>Sed ut perspiciatis unde omnis iste natus error sit volupta tem accusa ntium doloremque</p><a class="btn">Read More</a></div>
  </article>
</section>

<section class="section testimonials" role="img" aria-label="Red tinted photo of a business meeting behind customer testimonial">
  <h2 class="heading">TESTIMONIALS</h2>
  <div class="rule"></div>
  <div class="quote-mark">“</div>
  <blockquote>Sed ut perspiciatis unde omnis iste natus error sit voluptatem accusantium doloremque laudantium, totam rem aperiam eaque ipsa quae ab illo inv entore veritatis et quasi architecto beatae vitae dicta sunt explicabo emo enim ipsam voluptatem quia voluptas sit aspernatur aut odit aut fugit.</blockquote>
  <div class="divider"></div>
  <div class="name">MILO VARENTH</div>
  <div class="place">England</div>
  <div class="dots"><span class="on"></span><span></span><span></span><span></span></div>
</section>

<section class="section stats">
  <div class="stat"><strong>15,258</strong><span>Registered Consumers</span></div>
  <div class="stat"><strong>85+</strong><span>Countries reached</span></div>
  <div class="stat"><strong>11,250</strong><span>New Members</span></div>
  <div class="stat"><strong>160+</strong><span>API Partners</span></div>
</section>

<section class="section cta">
  <div class="cta-photo" role="img" aria-label="Photo of a businessman drawing a rising market chart over a city skyline"></div>
  <h2>Lorem Ipsum is simply dummy text of the printing</h2>
  <p>Sed ut perspiciatis unde omnis iste natus error sit volupta tem accusa ntium doloremque laudantium, totam rem aperiam, eaque ipsa quae ab illo inventore veritatis et quasi. Neque porro quisquam est, qui dolorem.</p>
  <a class="btn">Contact Us</a>
</section>

<footer class="section footer">
  <div class="logo"><span class="logo-dot"></span>TallyMarsh</div>
  <h5 style="left:481px">CONTACT US</h5>
  <ul class="f-contact">
    <li><svg width="10" height="14" viewBox="0 0 10 14"><path d="M5 0a5 5 0 0 0-5 5c0 4 5 9 5 9s5-5 5-9a5 5 0 0 0-5-5z" fill="#fff"/><circle cx="5" cy="5" r="2" fill="#262626"/></svg><span>318 Foundry Lane,<br>Carvell, IL 60517</span></li>
    <li><svg width="10" height="12" viewBox="0 0 10 12"><path d="M2 0l2 3-1 2c1 2 2 3 4 4l2-1 1 2-2 2C4 12 0 7 0 2z" fill="#fff"/></svg><span>555.014.2290</span></li>
    <li><svg width="12" height="10" viewBox="0 0 12 10"><rect width="12" height="10" fill="#fff"/><polyline points="0,0 6,5 12,0" fill="none" stroke="#262626"/></svg><span>info@tallymarsh.qevrobend.com</span></li>
  </ul>
  <h5 style="left:754px">MENU</h5>
  <ul class="f-menu"><li>Home</li><li>About Us</li><li>Services</li><li>Solutions</li><li>Blog</li><li>Contact Us</li></ul>
  <h5 style="left:943px">CONNECT WITH US</h5>
  <ul class="f-social"><li><i></i>Friendwall</li><li><i></i>Chirpline</li><li><i></i>Workgrid</li></ul>
  <div class="copyright">Copyright @ 2019 All Rights Reserved</div>
</footer>

</body>
</html>
```